Design mobile friendly real estate and property management company landing page

Design a clean, crisp modern looking landing page that is mobile-friendly (must resize, preferably using bootstrap framework). Landing page will consist of heading with login area, company info, body consists of company description and services, a list of available rental properties with photos, and a footer with additional links and info. Working on updating with text for text areas marked A, B, and C on the layout pdf, but in meantime, lorem ipsum is fine. I can connect events to most buttons, etc. Just need the bootstrap and html functionality set up. Previous company website (which should not be relied upon) is www.qlbt.net This is somewhat of a template for a start, but looking for a more professional and modern design for the new website. But this gives an idea of the content and what needs to be displayed, and how.

Target Market(s)

Clients looking for a property management company that is efficient and well-organized.

Industry/Entity Type

Property Management

Coding

Coded - Design and coding required

Number of Pages Required

1 page

Font styles to use
Sans Serif

Colors
0355a3

Requirements
Must have
• Resize for the screen using bootstrap.
• Navigation that collapses for mobile devices
• Large text boxes and good solid spacing around all elements.
Nice to have
• for property images it would be nice if they can be swiped on touch enabled devices (to the next or previous image). And have navigation that can be clicked to next or previous images.
• Would be nice if a captcha verification was included on contact form.
Should not have
• Fancy or eccentric art

```html
<!DOCTYPE html>
<html lang="en">
<head>
<meta charset="utf-8">
<title>Harbor Lane Realty</title>
<link href="https://fonts.googleapis.com/css2?family=Lato:ital,wght@0,400;0,700;1,400&family=Lora:wght@400;600&display=swap" rel="stylesheet">
<style>
:root{
  --navy:#1a2238;
  --navy-deep:#151c30;
  --ink:#222631;
  --muted:#6f7380;
  --line:#bfc3cc;
  --accent:#e8175d;
  --band:#f3f3f3;
  --white:#ffffff;
}
*{box-sizing:border-box;margin:0;padding:0}
html,body{width:1200px;height:2719px;overflow:hidden}
body{position:relative;background:var(--white);font-family:"Lato",Arial,sans-serif;color:var(--ink)}
.abs{position:absolute}
h1,h2{font-weight:400}

/* header */
.site-header{left:0;top:0;width:1200px;height:65px;background:var(--white)}
.brand{left:156px;top:20px;width:205px;text-align:center}
.brand-name{font-family:"Lora",Georgia,serif;font-size:18px;font-weight:600;letter-spacing:.3px;color:var(--ink);line-height:22px;white-space:nowrap}
.main-nav{left:476px;top:22px;display:flex;gap:26px;font-size:13px;color:#555;letter-spacing:.5px}
.main-nav .active{color:var(--ink);font-weight:700}
.nav-phone{left:838px;top:20px;font-size:15px;color:var(--ink);display:flex;align-items:center;gap:8px}
.nav-user{left:1020px;top:19px}

/* hero */
.hero{left:0;top:65px;width:1200px;height:399px;background:linear-gradient(180deg,#4a5470 0%,#6b6f82 35%,#7a6a5c 70%,#3c3a33 100%)}
.hero-title{left:0;top:198px;width:1200px;text-align:center;font-family:"Lora",Georgia,serif;font-size:30px;font-weight:600;color:var(--white);letter-spacing:.5px}
.hero-sub{left:0;top:240px;width:1200px;text-align:center;font-family:"Lora",Georgia,serif;font-size:14px;color:#eef;letter-spacing:.5px}
.search{left:350px;top:286px;width:497px;height:39px;background:var(--white);border-radius:20px;display:flex;overflow:hidden;font-size:12px}
.search-type{width:78px;display:flex;align-items:center;justify-content:center;gap:6px;color:#555;border-right:1px solid #ddd}
.search-input{flex:1;display:flex;align-items:center;padding-left:10px;color:#666}
.search-btn{width:135px;background:var(--navy);color:var(--white);display:flex;align-items:center;justify-content:space-between;padding:0 16px 0 28px;font-size:14px}

/* about */
.about-title{left:156px;top:522px;font-family:"Lora",Georgia,serif;font-size:28px;color:var(--ink)}
.about-text{left:156px;top:600px;width:400px;font-size:13.5px;line-height:17px;color:#555}
.btn-outline{border:1px solid #444;border-radius:16px;font-size:12px;color:#333;display:flex;align-items:center;justify-content:center}
.about-btn{left:156px;top:734px;width:161px;height:33px}
.about-photo{left:613px;top:520px;width:457px;height:245px;background:linear-gradient(180deg,#4d78c0 0%,#8ea6cc 45%,#8f7f6a 75%,#3e4a32 100%)}

/* listings */
.listings{left:0;top:827px;width:1200px;height:841px;background:var(--band)}
.section-title{left:0;width:1200px;text-align:center;font-family:"Lora",Georgia,serif;font-size:28px;color:var(--ink)}
.section-sub{left:0;width:1200px;text-align:center;font-size:13px;color:#333}
.card{width:279px;height:317px;overflow:hidden}
.card-name{position:absolute;left:0;right:0;bottom:12px;text-align:center;color:var(--white);font-size:19px;font-weight:700;white-space:nowrap}
.tag{position:absolute;left:0;top:8px;height:24px;padding:0 22px 0 10px;font-size:11px;font-weight:700;color:var(--white);line-height:24px;clip-path:polygon(0 0,100% 0,86% 100%,0 100%)}
.tag-sale{background:var(--accent)}
.tag-rent{background:var(--navy)}
.detail-panel{left:716px;top:935px;width:236px;height:350px;background:var(--white);border:1px solid #ddd;box-shadow:0 2px 8px rgba(0,0,0,.12);padding:30px 24px}
.detail-kind{font-size:12px;color:var(--accent);letter-spacing:.5px}
.detail-name{font-size:18px;color:var(--ink);margin-top:6px;white-space:nowrap}
.detail-region{font-size:13px;color:#666;margin-top:2px}
.detail-loc{font-size:11px;color:#999;margin-top:14px;display:flex;align-items:center;gap:6px}
.detail-text{font-size:10.5px;line-height:15px;color:#666;margin-top:22px}
.detail-price{font-size:16px;font-weight:700;color:var(--ink);margin-top:20px}
.detail-price span{font-size:11px;font-weight:400;color:#999}
.detail-btn{margin-top:22px;width:104px;height:31px;border-radius:16px;background:var(--navy);color:var(--white);font-size:12px;display:flex;align-items:center;justify-content:center}

/* testimonials */
.quote-text{left:285px;top:1776px;width:630px;text-align:center;font-style:italic;font-size:13.5px;line-height:18px;color:#888}
.client-name{left:0;top:1944px;width:1200px;text-align:center;font-size:13.5px;color:#333}
.client-role{left:0;top:1962px;width:1200px;text-align:center;font-style:italic;font-size:12px;color:#888}

/* map & footer */
.map{left:0;top:2027px;width:1200px;height:279px;background:linear-gradient(135deg,#e4e4e4,#d2d2d2 60%,#c8c8c8)}
.site-footer{left:0;top:2306px;width:1200px;height:413px;background:var(--navy-deep)}
.contact-card{left:460px;top:2147px;width:280px;height:433px;background:var(--white);padding:30px 20px 0}
.card-brand{text-align:center}
.card-brand .brand-name{font-size:15px;line-height:19px}
.contact-title{text-align:center;font-family:"Lora",Georgia,serif;font-size:19px;color:var(--ink);margin-top:14px}
.contact-sub{text-align:center;font-size:13px;color:#555;margin-top:2px}
.field{border:1px solid #aab;height:27px;margin-top:8px;font-size:11px;color:#aaa;padding:6px 8px}
.field-first{margin-top:22px}
.field-area{height:110px}
.send-btn{width:132px;height:30px;margin:16px auto 0}
.footer-head{font-family:"Lora",Georgia,serif;font-size:14px;color:var(--white)}
.quick-links{list-style:none;font-size:11.5px;color:#dde;line-height:19px}
.quick-links li::before{content:"";display:inline-block;width:4px;height:4px;background:#dde;border-radius:50%;margin-right:9px;vertical-align:middle}
.info{font-size:11.5px;color:#dde;line-height:16px}
.info-big{font-size:19px;color:var(--white);line-height:24px}
.socials{display:flex;gap:6px}
.socials span{width:15px;height:15px;border-radius:50%;background:#d8dbe3}
.foot-line{left:290px;top:2647px;width:620px;height:1px;background:#4a516a}
.foot-up{left:586px;top:2634px;width:26px;height:26px;border-radius:50%;border:1px solid #6b7290;background:var(--navy-deep)}
.copyright{top:368px;font-size:11.5px;color:#c8ccd8;white-space:nowrap}
</style>
</head>
<body>

<header class="site-header abs">
  <div class="brand abs">
    <div class="brand-name">HARBOR LANE REALTY</div>
  </div>
  <nav class="main-nav abs">
    <span class="active">Rent</span><span>Sell</span><span>Buy</span><span>Property</span><span>Agent</span><span>Finder</span>
  </nav>
  <div class="nav-phone abs">
    <svg width="16" height="16" viewBox="0 0 16 16"><circle cx="8" cy="8" r="7" fill="none" stroke="#222631" stroke-width="1.3"/><path d="M5.5 4.5l1.5 1.5-.8 1c.6 1.2 1.4 2 2.6 2.6l1-.8 1.5 1.5-1 1c-2.7-.4-5.4-3.1-5.8-5.8z" fill="#222631"/></svg>
    (055) 3104927
  </div>
  <svg class="nav-user abs" width="24" height="24" viewBox="0 0 24 24"><circle cx="12" cy="12" r="10.5" fill="none" stroke="#222631" stroke-width="1.4"/><circle cx="12" cy="10" r="3" fill="#222631"/><path d="M6.5 17.5c1.3-2.5 3.3-3.5 5.5-3.5s4.2 1 5.5 3.5" fill="#222631"/></svg>
</header>

<section class="hero abs" role="img" aria-label="Photograph of a modern two-storey house at dusk with lit windows and garages"></section>
<h1 class="hero-title abs">Discover Your Perfect Renta</h1>
<p class="hero-sub abs">Search nearby apartments, condos, and homes for rent</p>
<div class="search abs">
  <div class="search-type">Rent <svg width="8" height="5" viewBox="0 0 8 5"><path d="M1 1l3 3 3-3" fill="none" stroke="#555"/></svg></div>
  <div class="search-input">Search by Neighborhood, City</div>
  <div class="search-btn">Search <svg width="7" height="10" viewBox="0 0 7 10"><path d="M1 1l4 4-4 4" fill="none" stroke="#fff" stroke-width="1.5"/></svg></div>
</div>

<h2 class="about-title abs">About Harbor Lane Realty</h2>
<p class="about-text abs">Lorem Ipsum is simply dummy text of the printing and typesetting industry. Lorem Ipsum has been the industry's standard dummy text ever since the 1500s, when an unknown printer took a galley of type and scrambled it to make a type specimen book.</p>
<div class="btn-outline about-btn abs">Discover More About</div>
<div class="about-photo abs" role="img" aria-label="Photograph of a lit modern villa with stone facade at evening"></div>

<section class="listings abs"></section>
<h2 class="section-title abs" style="top:870px">Featured Listings</h2>
<p class="section-sub abs" style="top:911px">Lorem ipsum dolor sit amet</p>

<div class="card abs" style="left:156px;top:952px;background:linear-gradient(180deg,#5b86c8,#3a4454 70%,#2b2f36)" role="img" aria-label="Photograph of a tall modern apartment tower">
  <span class="tag tag-sale">SALE</span><span class="card-name">Cedar Point Tower</span></div>
<div class="card abs" style="left:459px;top:952px;background:linear-gradient(180deg,#a7a4dc,#7d6f8e 55%,#3d3a3a)" role="img" aria-label="Photograph of a Victorian style house at dusk">
  <span class="tag tag-rent">RENT</span><span class="card-name">Willow Crest Manor</span></div>
<div class="card abs" style="left:761px;top:952px;background:linear-gradient(180deg,#8fb0d8,#4e6a86 60%,#2e3a46)" role="img" aria-label="Photograph of a glass office tower">
  <span class="card-name">Cedar Point Tower</span></div>

<div class="card abs" style="left:156px;top:1293px;background:linear-gradient(180deg,#6e95d0,#9fb2c8 55%,#4a5a44)" role="img" aria-label="Photograph of a curved high-rise residential tower">
  <span class="tag tag-sale">SALE</span><span class="card-name">Silverline Heights</span></div>
<div class="card abs" style="left:459px;top:1293px;background:linear-gradient(180deg,#dcdcdc,#b7a892 50%,#4f5a3e)" role="img" aria-label="Photograph of a modern townhouse with garden">
  <span class="tag tag-rent">RENT</span><span class="card-name">Maple Row Residences</span></div>
<div class="card abs" style="left:761px;top:1293px;background:linear-gradient(180deg,#6aa3dc,#d9dde0 50%,#5a6d4a)" role="img" aria-label="Photograph of a white villa with a red tiled roof">
  <span class="card-name">Coral Bay Villa</span></div>

<aside class="detail-panel abs">
  <div class="detail-kind">VILLA</div>
  <div class="detail-name">Willow Crest Manor</div>
  <div class="detail-region">(Michigan)</div>
  <div class="detail-loc"><svg width="8" height="11" viewBox="0 0 8 11"><path d="M4 0a4 4 0 0 1 4 4c0 3-4 7-4 7S0 7 0 4a4 4 0 0 1 4-4z" fill="#aaa"/><circle cx="4" cy="4" r="1.5" fill="#fff"/></svg>Northern Ireland</div>
  <p class="detail-text">Lorem Ipsum is simply dummy text of the printing and typesetting industry. Lorem Ipsum has been the industry's standard dummy text ever</p>
  <div class="detail-price">Price: $50,000 <span>/ Per Month</span></div>
  <div class="detail-btn">See Details</div>
</aside>

<h2 class="section-title abs" style="top:1712px">What our clients say?</h2>
<p class="quote-text abs">Lorem Ipsum is simply dummy text of the printing and typesetting industry. Lorem Ipsum has been the industry's standard dummy text ever since the 1500s, when an unknown printer took a galley of type and scrambled it to make a type specimen book.</p>
<svg class="abs" style="left:476px;top:1882px" width="250" height="28" viewBox="0 0 250 28">
  <path d="M10 4L2 14l8 10" fill="none" stroke="#888" stroke-width="1.5"/>
  <path d="M240 4l8 10-8 10" fill="none" stroke="#888" stroke-width="1.5"/>
</svg>
<svg class="abs" style="left:536px;top:1864px" width="128" height="62" viewBox="0 0 128 62">
  <circle cx="24" cy="31" r="21" fill="#1a2238"/>
  <circle cx="104" cy="31" r="21" fill="#1a2238"/>
  <text x="13" y="38" fill="#fff" font-family="Lora,serif" font-size="18">“</text>
  <text x="106" y="38" fill="#fff" font-family="Lora,serif" font-size="18">”</text>
  <circle cx="64" cy="31" r="29" fill="#fff"/>
  <circle cx="64" cy="31" r="27" fill="#1a2238"/>
  <circle cx="64" cy="31" r="24" fill="#c89a7e" role="img" aria-label="Client portrait"/>
</svg>
<div class="client-name abs">Daniel Marsh</div>
<div class="client-role abs">(V.P. of Technologies)</div>

<div class="map abs" role="img" aria-label="Greyscale street map of the office neighbourhood"></div>

<footer class="site-footer abs">
  <div class="abs" style="left:219px;top:60px">
    <div class="footer-head">Quick Links</div>
    <ul class="quick-links" style="margin-top:18px">
      <li>Home</li><li>About Us</li><li>Rent</li><li>Sell</li><li>Buy</li><li>Property</li><li>Agent</li><li>Finder</li><li>Contact Us</li>
    </ul>
  </div>
  <div class="abs" style="left:809px;top:60px">
    <div class="footer-head">Contact Info</div>
    <div class="info" style="margin-top:22px">Address:<br>Lindenweg 12 40210<br>Northgate Offices</div>
    <div class="info" style="margin-top:16px">Call Today:</div>
    <div class="info-big">(041) 58 21 90 / 58 21 91</div>
    <div class="info" style="margin-top:12px">Email:<br>hello@harborlanerealty.com</div>
    <div class="socials" style="margin-top:12px"><span></span><span></span><span></span><span></span><span></span></div>
  </div>
  <div class="copyright abs" style="left:292px">© Copyright 2016 Harbor Lane Realty.</div>
  <div class="copyright abs" style="left:615px">Privacy Policy &nbsp; / &nbsp; Terms &amp; Condition &nbsp; / &nbsp; Cookies</div>
</footer>
<div class="foot-line abs"></div>
<div class="foot-up abs"><svg width="24" height="24" viewBox="0 0 24 24"><path d="M8 14l4-4 4 4" fill="none" stroke="#aab" stroke-width="1.3"/></svg></div>

<form class="contact-card abs">
  <div class="card-brand">
    <div class="brand-name">HARBOR LANE REALTY</div>
  </div>
  <div class="contact-title">Have any Questions ?</div>
  <div class="contact-sub">Contact Us</div>
  <div class="field field-first">Name</div>
  <div class="field">Email</div>
  <div class="field">Phone Number</div>
  <div class="field field-area">Type your message ...</div>
  <div class="btn-outline send-btn">Send Inquiry</div>
</form>

</body>
</html>
```